Lumo Fortunado superhero master

Full website makeover/update and redesign About a Public Figure.. in Spanish as well as English.
See current website at LumoFortunado.example and Chatterbook page LumoFortunates .
you can use any of the pictures and videos and be creative. page will be in English and Spanish same design.
think about a Lumo Superhero, like Kael from the lattice, with secret mystic knowledge, a combination of the character "Captain Vesper" mixed with the Millionaire Falcon of Harbor Row. Themes related to Mentor, based on zodiac, about Financial abundance using the stock Market.

Reason: designs are not what I like

Target Market(s)

USA hispanics Market

Number of Pages Required

5+ page

Colors

Designer to choose colors to be used in the design.

Requirements
Must have
• think about a Lumo Superhero, like Kael from the lattice, with secret mystic knowledge, a combination of the character "Captain Vesper" mixed with the Millionaire Falcon of Harbor Row. Themes related to Mentor, based on zodiac, about Financial abundance using the stock Market. Surprise me :)
Nice to have
• think about a Lumo Superhero, like Kael from the lattice, with secret mystic knowledge, a combination of the character "Captain Vesper" mixed with the falcon of harbor row.

```html
<!DOCTYPE html>
<html lang="en">
<head>
<meta charset="utf-8">
<title>LumoFortunates — Sign Up</title>
<link rel="stylesheet" href="https://fonts.googleapis.com/css2?family=Poppins:wght@500;600;700&family=Roboto:wght@400;500;700&display=swap">
<style>
:root{
  --green:#8cc63e;
  --green-dark:#7db532;
  --pink:#e8174f;
  --black:#0b0b0b;
  --grey-bg:#f2f2f2;
  --text:#222;
  --muted:#777;
  --gold:#d9a441;
}
*{box-sizing:border-box;margin:0;padding:0}
html,body{width:676px;height:1200px;overflow:hidden;background:#fff}
body{position:relative;font-family:"Roboto",sans-serif;color:var(--text)}
.abs{position:absolute}
.site-header{left:0;top:0;width:676px;height:66px;background:var(--black)}
.brand{display:flex;align-items:center;gap:6px}
.brand-mark{width:22px;height:22px;border-radius:50%;background:var(--gold)}
.brand-name{font-family:"Poppins",sans-serif;font-weight:700;color:var(--gold);font-size:14px;line-height:1;letter-spacing:.5px}
.top-meta{font-size:7px;color:#fff;display:flex;align-items:center;gap:4px;letter-spacing:.3px}
.contact-top{font-size:9.5px;color:#fff;display:flex;align-items:center;gap:6px;letter-spacing:.4px}
.icon-circle{width:22px;height:22px;border-radius:50%;background:var(--green);display:flex;align-items:center;justify-content:center}
.nav{left:0;width:676px;height:27px;background:var(--green);display:flex;padding-left:56px}
.nav a{width:94px;height:27px;display:flex;align-items:center;justify-content:center;color:#222;font-size:9.5px;text-decoration:none}
.nav a.active{background:var(--pink);color:#fff}
.nav.bottom a:nth-child(even){background:var(--green-dark)}
.hero{left:0;top:93px;width:676px;height:129px;background:linear-gradient(180deg,#2a2f2c 0%,#3d4440 50%,#1f2320 100%)}
.hero-title{left:0;top:134px;width:676px;text-align:center;font-family:"Poppins",sans-serif;font-weight:700;color:var(--green);font-size:21.5px;line-height:23px;letter-spacing:1.5px}
.intro{left:60px;top:243px;width:556px;text-align:center;color:var(--pink);font-size:9.5px;line-height:12px;letter-spacing:.4px}
.video{left:153px;top:279px;width:370px;height:195px;border:2px solid var(--green);background:linear-gradient(160deg,#1c1f1d,#0d0f0e 60%,#1a1d1b)}
.pricing{left:0;top:507px;width:676px;height:288px;background:var(--grey-bg)}
.divider{top:550px;width:1px;height:210px;background:#e0e0e0}
.price-badge{width:38px;height:38px;border-radius:50%;background:var(--green);border:3px solid #cfe7ad;color:#fff;font-family:"Poppins",sans-serif;font-weight:700;font-size:9px;line-height:9px;display:flex;flex-direction:column;align-items:center;justify-content:center}
.plan{width:150px;text-align:center}
.plan-title{color:var(--pink);font-weight:700;font-size:8px;letter-spacing:.4px;white-space:nowrap;margin:0 -20px}
.includes{color:var(--gold);font-size:6.5px;margin-top:6px;letter-spacing:.3px}
.bonus{font-size:6.5px;font-weight:500;margin:4px 0 3px;letter-spacing:.2px}
.plan ul{list-style:none}
.plan li{font-size:7px;line-height:8.5px;letter-spacing:.4px;margin-top:3px;color:#333}
.plan li::before,.mastermind li::before{content:"›";color:var(--pink);margin-right:5px;font-weight:700}
.btn{background:var(--pink);color:#fff;font-size:8.5px;letter-spacing:1.5px;display:flex;align-items:center;justify-content:center;width:78px;height:22px;text-decoration:none}
.book{left:80px;top:549px;width:130px;height:130px;border-radius:50%;background:radial-gradient(circle at 45% 50%,#2b3fa0 0%,#1a2460 40%,#ffffff 72%);box-shadow:0 2px 6px rgba(0,0,0,.15)}
.mastermind{left:56px;top:820px;width:564px;height:199px;background:#f4f4f4;border:1px solid #ddd;box-shadow:0 2px 4px rgba(0,0,0,.2)}
.mm-price{color:var(--pink);font-family:"Poppins",sans-serif;font-weight:700;font-size:17px}
.mm-note{font-size:5.5px;color:var(--muted);letter-spacing:.4px}
.mm-heading{color:var(--green);font-family:"Poppins",sans-serif;font-weight:600;font-size:17px;line-height:20px;letter-spacing:1.5px}
.mm-lead{font-size:7px;font-weight:500;letter-spacing:.3px}
.mastermind ul{list-style:none}
.mastermind li{font-size:7px;line-height:12px;letter-spacing:.3px;color:#333}
.footer{left:0;top:1042px;width:676px;height:131px;background:var(--black);color:#fff}
.foot-heading{font-family:"Poppins",sans-serif;font-weight:500;font-size:11px;letter-spacing:1.5px;color:#fff}
.foot-item{display:flex;align-items:center;gap:9px;font-size:7px;color:#ddd;letter-spacing:.4px}
.foot-item .icon-circle{width:17px;height:17px}
.copyright{font-size:7px;color:#ccc;letter-spacing:.6px}
.email-input{left:442px;top:1086px;width:178px;height:19px;background:#2a2a2a;color:#999;font-size:7px;padding-left:9px;display:flex;align-items:center;letter-spacing:.4px}
.subscribe{left:442px;top:1115px;width:178px;height:19px;background:var(--pink);color:#fff;font-size:7px;letter-spacing:.6px;display:flex;align-items:center;justify-content:center}
</style>
</head>
<body>

<header class="abs site-header">
  <div class="abs brand" style="left:56px;top:20px">
    <span class="brand-mark"></span>
    <span class="brand-name">LUMO FORTUNATES</span>
  </div>
  <div class="abs top-meta" style="left:478px;top:12px">
    <svg width="14" height="10" viewBox="0 0 14 10"><circle cx="5" cy="5" r="4" fill="none" stroke="#8cc63e" stroke-width="1.2"/><path d="M5 2.5v2.7l1.8 1" stroke="#8cc63e" fill="none" stroke-width="1"/></svg>
    24/7 SUPPORT
  </div>
  <div class="abs top-meta" style="left:566px;top:12px">
    <span style="width:10px;height:10px;border-radius:50%;background:#c8d2e8;display:inline-block"></span>
    ENGLISH ▾
  </div>
  <div class="abs contact-top" style="left:344px;top:34px">
    <span class="icon-circle"><svg width="11" height="11" viewBox="0 0 24 24"><path fill="#fff" d="M6.6 10.8a15 15 0 006.6 6.6l2.2-2.2a1 1 0 011-.25 11 11 0 003.6.6 1 1 0 011 1V20a1 1 0 01-1 1A17 17 0 013 4a1 1 0 011-1h3.5a1 1 0 011 1c0 1.250.2 2.450.57 3.57a1 1 0 01-.25 1z"/></svg></span>
    (555) 014-2290
  </div>
  <div class="abs contact-top" style="left:469px;top:34px">
    <span class="icon-circle"><svg width="11" height="9" viewBox="0 0 22 16"><rect x="1" y="1" width="20" height="14" fill="none" stroke="#fff" stroke-width="2"/><path d="M1 1l10 8 10-8" fill="none" stroke="#fff" stroke-width="2"/></svg></span>
    info@LumoFortunates.example
  </div>
</header>

<nav class="abs nav" style="top:66px">
  <a href="#">Home</a><a href="#" class="active">Sign up</a><a href="#">How It Works</a><a href="#">About Lumo</a><a href="#">Videos</a><a href="#">FAQ</a>
</nav>

<section class="abs hero" role="img" aria-label="Dimmed photo of a trading floor with market screens"></section>
<h1 class="abs hero-title">WHAT ARE YOU WAITING FOR?<br>UNLOCK YOUR POTENTIAL!</h1>

<p class="abs intro">With the LumoAlerts &amp; LumoCoach system, you can make thousands in minutes!Learn the strategy and get mentored by LumoFortunado</p>

<div class="abs video" role="img" aria-label="Video preview of a stock trading platform with charts">
  <svg class="abs" style="left:166px;top:78px" width="36" height="36" viewBox="0 0 36 36"><circle cx="18" cy="18" r="18" fill="#8cc63e"/><path d="M14 10l12 8-12 8z" fill="#fff"/></svg>
</div>

<section class="abs pricing"></section>
<div class="abs divider" style="left:242px"></div>
<div class="abs divider" style="left:434px"></div>

<div class="abs book" role="img" aria-label="Stock market guide book and DVD"></div>
<div class="abs price-badge" style="left:126px;top:532px"><span>$</span><span>99</span></div>
<div class="abs price-badge" style="left:319px;top:532px"><span>$</span><span>369</span></div>
<div class="abs price-badge" style="left:512px;top:532px"><span>$</span><span>1,200</span></div>

<div class="abs plan" style="left:70px;top:689px">
  <div class="plan-title">VIDEO GUIDE AND PDF</div>
  <div class="includes">INCLUDES:</div>
  <ul><li>Video Guide &amp; Pdf. <span style="font-size:6px">(Check your email for link)</span></li></ul>
</div>
<div class="abs plan" style="left:263px;top:585px">
  <div class="plan-title">3-MONTH &nbsp;ALERT SUBSCRIPTION</div>
  <div class="includes">INCLUDES:</div>
  <ul><li>3 months LumoAlerts- Buys &amp;<br>Sells trade alerts.</li></ul>
  <div class="bonus">EXTRA BONUS INCLUDED:</div>
  <ul>
    <li>Video Class &amp; Book PDF Guide downloads.</li>
    <li>Private Group in Chatterbook "LumoFortunados".</li>
    <li>Practice account &amp; live quotes.</li>
    <li>Private chat after 5pm.</li>
  </ul>
</div>
<div class="abs plan" style="left:456px;top:585px">
  <div class="plan-title">12-MONTH ALERTS SUBSCRIPTION</div>
  <div class="includes">INCLUDES:</div>
  <ul><li>One on one Class with Lumo &amp;<br>12 months of LumoVipAlerts.</li></ul>
  <div class="bonus">EXTRA BONUS INCLUDED:</div>
  <ul>
    <li>Direct Chat with LumoFortunado 9am-4pm.</li>
    <li>Book PDF Guide &amp; Lumocoach Video Class.</li>
    <li>Private Group in Chatterbook "LumoFortunados".</li>
    <li>Practice account with live quotes.</li>
  </ul>
</div>
<a class="abs btn" href="#" style="left:106px;top:749px">BUY NOW</a>
<a class="abs btn" href="#" style="left:299px;top:749px">BUY NOW</a>
<a class="abs btn" href="#" style="left:492px;top:749px">BUY NOW</a>

<section class="abs mastermind">
  <div class="abs" style="left:16px;top:21px">
    <div class="mm-price">$5,000</div>
    <div class="mm-note">ONLY ONE PAYMENT</div>
  </div>
  <h2 class="abs mm-heading" style="left:96px;top:21px">Want to accelerate your progress?<br>Join Lumo in a Mastermind Group!</h2>
  <p class="abs mm-lead" style="left:96px;top:66px">The LumoCoach One on One. WOrk One on One with Dario LumoFortunado, He will teach you everything he knows.</p>
  <div class="abs includes" style="left:96px;top:78px">INCLUDES:</div>
  <ul class="abs" style="left:96px;top:93px">
    <li>LumoAlerts Vip for a lifetime.</li>
    <li>Coaching Class With Dario "LumoFortunado" on how to find your passion, and becoming a Millionaire.</li>
    <li>Open chat Vip during market hours.</li>
    <li>Demo practice app with live quotes.</li>
  </ul>
  <a class="abs btn" href="#" style="left:97px;top:152px">BUY NOW</a>
</section>

<footer class="abs footer"></footer>
<div class="abs brand" style="left:56px;top:1082px">
  <span class="brand-mark"></span>
  <span class="brand-name">LUMO FORTUNATES</span>
</div>
<div class="abs copyright" style="left:67px;top:1122px">© 2017 &nbsp;| &nbsp;All Rights Reserved.</div>

<div class="abs foot-heading" style="left:252px;top:1064px">CONTACT US</div>
<div class="abs foot-item" style="left:253px;top:1084px">
  <span class="icon-circle"><svg width="9" height="9" viewBox="0 0 24 24"><path d="M2 5l6-2 8 3 6-2v15l-6 2-8-3-6 2z M8 3v16 M16 6v16" fill="none" stroke="#111" stroke-width="2"/></svg></span>Palmview, FL 00000, USA
</div>
<div class="abs foot-item" style="left:253px;top:1107px">
  <span class="icon-circle"><svg width="9" height="9" viewBox="0 0 24 24"><path fill="#111" d="M6.6 10.8a15 15 0 006.6 6.6l2.2-2.2a1 1 0 011-.25 11 11 0 003.6.6 1 1 0 011 1V20a1 1 0 01-1 1A17 17 0 013 4a1 1 0 011-1h3.5a1 1 0 011 1c0 1.250.2 2.450.57 3.57a1 1 0 01-.25 1z"/></svg></span>(555) 014-2290
</div>
<div class="abs foot-item" style="left:253px;top:1130px">
  <span class="icon-circle"><svg width="9" height="7" viewBox="0 0 22 16"><rect x="1" y="1" width="20" height="14" fill="none" stroke="#111" stroke-width="2"/><path d="M1 1l10 8 10-8" fill="none" stroke="#111" stroke-width="2"/></svg></span>info@LumoFortunates.example
</div>

<div class="abs foot-heading" style="left:442px;top:1064px">SUBSCRIBE NEWSLETTER</div>
<div class="abs email-input">Enter email...</div>
<div class="abs subscribe">SUBSCRIBE</div>

<nav class="abs nav bottom" style="top:1173px">
  <a href="#">Home</a><a href="#">Sign up</a><a href="#">How It Works</a><a href="#">Abut Lumo</a><a href="#">Videos</a><a href="#">FAQ</a>
</nav>

</body>
</html>
```